Artwork for Space/Ambient/Drone synthesizer music

Art work is needed for a Collection of ambient type synthesizer soundtrack type of music. Title of album is Drift Logs Vol. 1. This album's theme were to be kept as Movie music & Game music.

Looking for art reminiscent of Rune Halvik retro futuristic look. Open to any ideas but I would like to see primarily sci-fi themes. I would like to have my logo either top center or bottom center and title of album top center or bottom center.

Online distributor requires art to be 2000 x 2000 at minimum but larger is preferable and no bigger than 10mb.

Track list with time is as follows:

1. Far Lantern 05:20
2. Moonwake 10:09
3. Tides 02:31
4. Hush 04:39
5. Paper Tenant 03:55
6. Velvet Echo 03:13
7. Stillwater 03:40
8. Unmoored 06:03
9. Lullabies 02:06

I have uploaded 7 images by Rune Halvik as reference for you (do not use those as I don't have rights to them). My logo is also uploaded for you to use in the art.

Target Market(s)

Synthwave. Retrowave. Ambient/Drone

Industry/Entity Type

Music Download

Font styles to use
Decorative

Colors

Designer to choose colors to be used in the design.

Requirements
Must have
• My logo (provided). Can change color of logo to fit art work.
Nice to have
• Abstract art is welcome.
Should not have
• No drug references. No death references. No references to countries. No graffiti style of art. No vector 80s graphics. No prominent faces. No religious references.

```html
<!DOCTYPE html>
<html lang="en">
<head>
<meta charset="utf-8">
<title>Drift Logs Vol. 1 — Album Cover</title>
<link rel="stylesheet" href="https://fonts.googleapis.com/css2?family=Audiowide&display=swap">
<style>
  :root {
    --space-deep: #05080d;
    --space-mid: #0b1119;
    --nebula-violet: #2a1630;
    --ember: #e8703f;
    --ember-soft: #f08a55;
    --planet-light: #c45a3c;
    --planet-dark: #2a140e;
    --rim-glow: #ffb58a;
    --hud-line: rgba(170, 180, 200, 0.12);
    --band-light: rgba(200, 190, 210, 0.10);
  }
  html, body {
    margin: 0;
    padding: 0;
    width: 1200px;
    height: 1199px;
    overflow: hidden;
    background: var(--space-deep);
  }
  .cover {
    position: relative;
    width: 1200px;
    height: 1199px;
    overflow: hidden;
    background:
      radial-gradient(ellipse 620px 420px at 560px 300px, rgba(160, 70, 40, 0.45), transparent 70%),
      radial-gradient(ellipse 500px 360px at 900px 380px, rgba(70, 30, 80, 0.45), transparent 70%),
      radial-gradient(ellipse 500px 400px at 820px 860px, rgba(120, 50, 20, 0.35), transparent 70%),
      linear-gradient(180deg, var(--space-mid) 0%, #120d12 45%, var(--space-deep) 100%);
  }
  .hud-overlay {
    position: absolute;
    inset: 0;
    width: 1200px;
    height: 1199px;
  }
  .light-band {
    position: absolute;
    left: 0;
    height: 30px;
    background: linear-gradient(90deg, transparent, var(--band-light) 20%, var(--band-light) 80%, transparent);
  }
  .light-band--upper { top: 292px; width: 1020px; height: 34px; }
  .light-band--title { top: 316px; width: 1115px; height: 70px; background: linear-gradient(90deg, rgba(255,180,140,0.06), rgba(200,200,230,0.14) 50%, rgba(120,160,200,0.08)); }
  .light-band--lower { top: 405px; width: 820px; height: 18px; }
  .planet {
    position: absolute;
    left: 0;
    top: 0;
    width: 1200px;
    height: 1199px;
  }
  .album-title {
    position: absolute;
    left: 19px;
    top: 326px;
    margin: 0;
    font-family: "Audiowide", sans-serif;
    font-weight: 400;
    font-size: 58px;
    line-height: 1;
    letter-spacing: 1px;
    color: var(--ember);
    white-space: nowrap;
  }
  .artist-mark {
    position: absolute;
    left: 0;
    width: 1200px;
    top: 955px;
    margin: 0;
    text-align: center;
    font-family: "Audiowide", sans-serif;
    font-size: 40px;
    letter-spacing: 4px;
    color: var(--ember);
  }
</style>
</head>
<body>
<main class="cover">
  <div class="light-band light-band--upper"></div>
  <div class="light-band light-band--title"></div>
  <div class="light-band light-band--lower"></div>

  <svg class="hud-overlay" viewBox="0 0 1200 1199" aria-hidden="true">
    <g fill="none" stroke="var(--hud-line)" stroke-width="2">
      <circle cx="600" cy="560" r="380"/>
      <circle cx="760" cy="420" r="300"/>
      <path d="M40 430 A620 620 0 0 1 520 170"/>
      <path d="M740 460 A420 420 0 0 1 1120 740"/>
    </g>
  </svg>

  <svg class="planet" viewBox="0 0 1200 1199" role="img" aria-label="Photograph of a red cratered planet rising from the bottom, its lit rim glowing orange against dark space">
    <defs>
      <radialGradient id="planetSurface" cx="0.55" cy="0.1" r="0.8">
        <stop offset="0" stop-color="var(--planet-light)"/>
        <stop offset="0.35" stop-color="#8a3a26"/>
        <stop offset="0.7" stop-color="var(--planet-dark)"/>
        <stop offset="1" stop-color="#0a0808"/>
      </radialGradient>
      <linearGradient id="planetFade" x1="0" y1="0" x2="0" y2="1">
        <stop offset="0.3" stop-color="#05080d" stop-opacity="0"/>
        <stop offset="1" stop-color="#05080d" stop-opacity="0.85"/>
      </linearGradient>
    </defs>
    <ellipse cx="600" cy="1620" rx="1150" ry="1110" fill="url(#planetSurface)"/>
    <ellipse cx="600" cy="1620" rx="1150" ry="1110" fill="url(#planetFade)"/>
    <ellipse cx="600" cy="1620" rx="1150" ry="1110" fill="none" stroke="var(--rim-glow)" stroke-opacity="0.55" stroke-width="3"/>
  </svg>

  <svg class="hud-overlay" viewBox="0 0 1200 1199" aria-hidden="true">
    <g fill="none" stroke="var(--hud-line)" stroke-width="2">
      <path d="M980 520 A520 520 0 0 1 560 1150"/>
      <line x1="0" y1="960" x2="950" y2="960"/>
    </g>
  </svg>

  <h1 class="album-title">DRIFT LOGS Vol.1</h1>
  <p class="artist-mark">KESTREL TONE</p>
</main>
</body>
</html>
```